Business and Success Coaching Business Card

Need a business card for my coaching business. I coach small businesses, career professionals and, individuals wanting to unlock their human potential and achieve excellence. At the heart of our methodology is the Shaping Purposeful Action Routines Knowingly (SPARK) approach to formulate empowerment, create principles for success and setting achievable outcomes. I would like something that incorporates our new logo, something clean and sharp with a solid darker, but complementary background, color on the card front. The back should be white where there will be room for three questions

Target Market(s)

People looking to advance and improve themselves through a success coach

Industry/Entity Type

Life Coaching

Contact Information for Business Card

Contact information on card.
Business name on front of card
Questions on back

Font styles to use
Other font styles liked:
• Century Gothic or other Serif style fonts that look similar to Century Gothic

Colors

Designer to choose colors to be used in the design.

Requirements
Must have
• Logo on front of card
• Business name - The Steady Forge
• Contact name - Ted Harlow
• Address - Box 4619, Littleton, CO 80127-4619
• Phone number - 303-555-0147
• Email address - harlow.ted@thesteadyforge.example
• Certifications - CSC, CCHt, PTT, PNLP
• Back of card
• Three questions on the back of the card:
• If you were at your best, what would you do right now?
• What is the decision you have been avoiding?
• What's one action you could take in the next 10 minutes?
Nice to have
• I would like to see a solid color on the front of the card that compliments the logo.
• Back should be white, or could be contrasting, but need to have the three questions.

```html
<!DOCTYPE html>
<html lang="en">
<head>
<meta charset="utf-8">
<title>The Steady Forge – Business Card</title>
<link href="https://fonts.googleapis.com/css2?family=Didact+Gothic&family=Questrial&display=swap" rel="stylesheet">
<style>
  :root {
    --page: #2b2b2d;
    --white: #ffffff;
    --sky: #4a87c8;
    --sky-light: #7fb2ea;
    --navy: #1f3a78;
    --navy-deep: #1a3170;
    --ink: #2a3f86;
    --figure: #4f8acb;
    --rule: #3a4f8f;
    --faint: #eef1f6;
  }
  * { box-sizing: border-box; margin: 0; padding: 0; }
  html, body { width: 1200px; height: 900px; overflow: hidden; }
  body {
    background: var(--page);
    font-family: "Didact Gothic", "Questrial", sans-serif;
    position: relative;
  }
  .card {
    position: absolute;
    left: 250px;
    width: 700px;
    height: 400px;
    overflow: hidden;
  }

  /* ---------- back ---------- */
  .card-back { top: 40px; background: var(--white); }
  .card-back .band-top {
    position: absolute; top: 0; left: 0; right: 0; height: 9px; background: var(--sky);
  }
  .card-back .band-bottom {
    position: absolute; bottom: 0; left: 0; right: 0; height: 11px; background: var(--navy-deep);
  }
  .card-back .faint-name {
    position: absolute; right: 30px; bottom: 28px;
    font-size: 52px; color: var(--faint); letter-spacing: 1px; white-space: nowrap;
  }
  .card-back .figure-area {
    position: absolute; left: 40px; top: 95px; width: 200px; height: 220px;
    border-radius: 40% 40% 30% 30%;
    background: radial-gradient(ellipse at center, var(--figure) 0%, rgba(79,138,203,0.55) 55%, rgba(79,138,203,0) 72%);
  }
  .questions {
    position: absolute; left: 252px; right: 24px; top: 80px;
    list-style: none;
  }
  .questions li {
    color: var(--ink);
    font-size: 15px;
    white-space: nowrap;
    padding-bottom: 10px;
    margin-bottom: 34px;
    border-bottom: 1.5px dotted var(--rule);
    letter-spacing: 0.2px;
  }

  /* ---------- front ---------- */
  .card-front { top: 460px; background: var(--sky); }
  .card-front svg.wave { position: absolute; inset: 0; }
  .brand {
    position: absolute; left: 40px; top: 118px;
    display: flex; align-items: center; gap: 12px;
  }
  .brand .mark {
    width: 22px; height: 22px; border-radius: 50%; background: var(--navy);
  }
  .brand .name { font-size: 34px; color: var(--navy); white-space: nowrap; }
  .contact {
    position: absolute; right: 32px; top: 80px;
    text-align: right; color: var(--white);
  }
  .contact .person { font-size: 19px; color: var(--sky-light); letter-spacing: 1px; font-weight: 700; }
  .contact .certs { font-size: 15px; margin-top: 4px; }
  .contact .lines { margin-top: 20px; }
  .contact .line {
    display: flex; justify-content: flex-end; align-items: center; gap: 8px;
    font-size: 15px; margin-top: 6px; white-space: nowrap;
  }
  .contact .line svg { width: 13px; height: 13px; flex: none; }
  .address {
    position: absolute; left: 40px; bottom: 34px;
    color: var(--white); font-size: 16px; white-space: nowrap;
  }
</style>
</head>
<body>

  <section class="card card-back" aria-label="Card back">
    <div class="band-top"></div>
    <div class="faint-name" aria-hidden="true">The Steady Forge</div>
    <div class="figure-area" role="img" aria-label="Blue silhouette of a person leaping with arms outstretched"></div>
    <ol class="questions">
      <li>If you were at your best, what would you do right now?</li>
      <li>What is the decision you have been avoiding?</li>
      <li>What's one action you could take in the next 10 minutes?</li>
    </ol>
    <div class="band-bottom"></div>
  </section>

  <section class="card card-front" aria-label="Card front">
    <svg class="wave" viewBox="0 0 700 400" preserveAspectRatio="none" aria-hidden="true">
      <path d="M0,300 C180,305 300,300 410,180 C500,80 590,30 700,15 L700,400 L0,400 Z" fill="var(--navy)"/>
      <path d="M200,330 C330,300 410,200 490,120 C560,55 630,28 700,22" fill="none" stroke="var(--sky)" stroke-width="9"/>
      <path d="M180,345 C320,320 400,215 485,130 C555,65 630,40 700,36" fill="none" stroke="var(--navy-deep)" stroke-width="4"/>
    </svg>

    <div class="brand">
      <span class="mark" aria-hidden="true"></span>
      <span class="name">The Steady Forge</span>
    </div>

    <div class="contact">
      <div class="person">TED HARLOW</div>
      <div class="certs">CSC, CCHt, PTT, PNLP</div>
      <div class="lines">
        <div class="line">303-555-0147
          <svg viewBox="0 0 16 16"><circle cx="8" cy="8" r="7.2" fill="none" stroke="#fff" stroke-width="1.4"/><path d="M5.5 4.5l1.5 0 .6 1.8-.9.7c.5 1 1.2 1.7 2.2 2.2l.7-.9 1.8.6v1.5c-3.5.2-6.1-2.4-5.9-5.9z" fill="#fff"/></svg>
        </div>
        <div class="line">harlow.ted@thesteadyforge.example
          <svg viewBox="0 0 16 16"><rect x="2" y="4" width="12" height="8" fill="none" stroke="#fff" stroke-width="1.4"/><path d="M2 4l6 5 6-5" fill="none" stroke="#fff" stroke-width="1.4"/></svg>
        </div>
        <div class="line">www.thesteadyforge.example
          <svg viewBox="0 0 16 16"><circle cx="8" cy="8" r="6.5" fill="none" stroke="#fff" stroke-width="1.4"/><ellipse cx="8" cy="8" rx="2.8" ry="6.5" fill="none" stroke="#fff" stroke-width="1.2"/><path d="M1.5 8h13" stroke="#fff" stroke-width="1.2"/></svg>
        </div>
      </div>
    </div>

    <div class="address">Box 4619, Littleton, CO 80127-4619</div>
  </section>

</body>
</html>
```